N.5 HTML Media Template for Virtual Assistant card

We need the development of 5 interactive and optimized web card templates, each designed specifically for a different type of topic. These templates will initially be displayed in a chat client on both desktop and mobile devices, and subsequently shared across major social networks. The cards will serve as response balloons in the chat for queries related to various topics such as local business searches, news, history, sports, etc. Each template will be tailored to optimize the presentation of specific content for each topic.The goal is to create cards that capture user attention through engaging designs, easily readable text, and light animations, while ensuring excellent cross-platform compatibility and rapid loading speed both in the chat client context and across various social media video formats. The content of the cards should be designed to be effective in a chat card loop, providing an engaging and informative user experience.The cards will be used in specific video formats for platforms like Pintaro Feed, Glimmora Loops, VidRoost Snips, WorkNest Video, and ZipZap, with detailed technical specifications provided below. The project requires the use of modern web technologies, such as HTML5, inline CSS, and JavaScript, with a focus on performance optimization and adherence to web accessibility standards.

We require the development of a web page that meets the following criteria:

Responsive Design: The page must be optimized to adapt perfectly to the resolutions used by the most popular social networks, ensuring a smooth and consistent user experience on all devices (smartphones, tablets, desktops).
Text: The page should contain easily readable text, which may include rather lengthy texts.
Images: Inclusion of standard images and panoramic images (360 degrees).
Animations: Use lightweight animations to enhance interactivity without compromising page loading speed.
Inline Styles: Prefer the use of inline styles for better management and performance.
External Scripts: The use of external scripts is allowed as long as they are hosted on reliable CDNs. However, it's essential that these scripts are lightweight and do not negatively impact the page loading speed.

The page should be lightweight and designed with a strong focus on loading speed.
Implementation of optimization techniques such as lazy loading, image compression, and code minification.
The page must comply with web accessibility standards.
Ensure that all content is accessible and easily navigable.
The cards must be created in HTML5.
The CSS must be inline and compatible with:

last 1 Chrome version
last 1 Firefox version
last 2 Edge major versions
last 2 Safari major versions
last 2 iOS major versions
Firefox ESR
Inline JavaScript and fast CDN-loaded scripts are allowed and should be executed on 'DOMContentLoaded' of the card (include a loading spinner).
All cards must be responsive.
All cards must respond (via CSS media queries) to a specific format related to the social platform and the video format to be created.
List of social video formats:
Pintaro Feed Video:
Recommended dimensions: 1280 x 720 pixels for both landscape and portrait
Minimum width: 1200 pixels
Supported ratios: 16:9 (landscape), 9:16 (full portrait)

Pintaro Tales:
Recommended size: 1080 x 1080 pixels
Minimum size: 600 x 600 pixels (1:1 aspect ratio)
Aspect ratios: from 1.91 to 9:16, with gradient-colored bars above and below videos less than 9:16

Pintaro Loops:
Resolution: minimum 540 x 960 (540p) (recommended 1080×1920 or higher)
Supported aspect ratios: 9:16

Glimmora in-feed video:
Video landscape: 1920 by 1080 pixels (16:9 aspect ratio)
Square video: 1080 by 1080 pixels (1:1 aspect ratio)
Vertical video: 1080 by 1350 pixels (4:5 aspect ratio)

Glimmora Loops:
Supported aspect ratios: 0.01:1-10:1 (9:16 recommended)

Glimmora Tales Video:
Recommended size: 1080px by 1080px pixels
Minimum size: 600 x 1067

Q landscape videos:
Recommended size: 1280 by 720 pixels
Supported aspect ratios: 16:9

Q Portrait and Square Videos:
Recommended sizes: 720×1280 (portrait), 720 by 720 pixels (square)

VidRoost Video:
Recommended sizes:
426 by 240 pixels (240p)
640 by 360 pixels (360p)
854 by 480 pixels (480p)
1280 by 720 pixels (720p)
1920 by 1080 pixels (1080p)
2560 by 1440 pixels (1440p)
3840 by 2160 pixels (2160p)
Supported aspect ratios: 16:9 and 4:3

VidRoost Snips:
Recommended sizes:
240 by 426 pixels (240p)
360 by 640 pixels (360p)
480 by 854 pixels (480p)
720 by 1280 pixels (720p)

WorkNest Video:
Maximum size: 4,096 by 2,304 pixels
Supported aspect ratios: from 1:2.4 to 2.4:1

ZipZap:
Format 9:16 (portrait)
Recommended dimensions: 1920 by 1080 pixels (1080p)

We need the UI and implementation of 5 cards with animations, which will first be inserted into a virtual assistant chat (like rovo chat), and then shared on social networks as videos(Our system generates an mp4 of the animation). The cards contain images (from pelmo image API), text and 360-degree overviews, for local activities for example. We need them to be designed according to the type of information they contain, so with different animations depending on the type of card. Example: a response that contains 1) card about a business (as in the figma I sent you), or a response that contains 2) information about a sporting event (images attached), 3) Web search, 4) News, 5) product card. The cards should have the characteristics indicated in the brief .The images we have available, related to the responses in the chat, are generated via real-time api calls, along with the ai responses, cannot be edited or cropped, and are often small in size.

The attached figma and video and pictures are just an example to make it clear what they are for. We want creative design that is not something already seen and traditional. Be creative.

https://www.protoboardly.example/proto/83hQwLpZ2vXmTrk9BsaNcd/TEVO-TILE?page-id=0%3A1&type=design&node-id=512-7741&viewport=1902%2C6620%2C0.5&t=kPq4ZmW8rLx2aYbe-3&scaling=min-zoom&starting-point-node-id=507%3A1180

https://www.protoboardly.example/proto/83hQwLpZ2vXmTrk9BsaNcd/TEVO-TILE?page-id=0%3A1&type=design&node-id=512-7906&viewport=1902%2C6620%2C0.5&t=kPq4ZmW8rLx2aYbe-3&scaling=min-zoom&starting-point-node-id=507%3A1180&mode=design

In attachment, a very ugly and rudimentary example

Target Market(s)

B2C

Industry/Entity Type

media content

Coding

Coded - Design and coding required

Colors
00AB8E
00BBA5
67D7C9
C6EFE9
E9F9F6

Requirements
Must have
• Innovative, Engaging
Nice to have
• Card not seen before
Should not have
• Traditional card

```html
<!DOCTYPE html>
<html lang="en">
<head>
<meta charset="utf-8">
<title>Chat – Sports Card</title>
<link rel="stylesheet" href="https://fonts.googleapis.com/css2?family=Open+Sans:wght@400;600;700&family=Roboto:wght@400;500;700&display=swap">
<style>
  :root{
    --green-deep:#00AB8E;
    --green:#00BBA5;
    --green-soft:#67D7C9;
    --mint:#C6EFE9;
    --mint-pale:#E9F9F6;
    --white:#ffffff;
    --ink:#4a4a4a;
    --muted:#9a9a9a;
  }
  *{box-sizing:border-box;margin:0;padding:0}
  html,body{width:1200px;height:2597px;overflow:hidden;background:var(--white);position:relative}
  .screen{
    position:absolute;left:0;top:0;width:390px;height:844px;
    transform:scale(3.0769);transform-origin:0 0;
    background:var(--white);font-family:"Open Sans",sans-serif;overflow:hidden;
  }
  .app-bar{position:absolute;left:0;top:0;width:390px;height:70px;background:var(--white)}
  .app-bar__back{position:absolute;left:24px;top:25px}
  .app-bar__title{position:absolute;left:0;right:0;top:20px;text-align:center;font-family:"Roboto",sans-serif;font-size:24px;line-height:30px;color:var(--ink);font-weight:400}
  .app-bar__menu{position:absolute;left:345px;top:26px}

  .contact-bar{position:absolute;left:0;top:70px;width:390px;height:46px;background:var(--green-deep);color:var(--white);font-family:"Roboto",sans-serif}
  .contact-bar__avatar{position:absolute;left:23px;top:6px;width:34px;height:34px;border-radius:50%;background:radial-gradient(circle at 50% 40%,#b98a6a 0 35%,#2b2f3a 36%);border:1.5px solid var(--white)}
  .contact-bar__name{position:absolute;left:65px;top:12px;font-size:17px;line-height:22px;font-weight:700}
  .contact-bar__status{position:absolute;right:22px;top:14px;font-size:15px;line-height:18px;font-weight:400}

  .conversation{position:absolute;left:0;top:116px;width:390px;height:719px;background:var(--mint-pale)}

  .bubble-sent{position:absolute;left:130px;top:284px;width:237px;height:36px;border-radius:18px;background:var(--green-deep);color:var(--white);font-size:12.5px;font-weight:600;line-height:36px;text-align:center;white-space:nowrap}
  .timestamp{position:absolute;right:23px;font-size:9px;line-height:11px;color:var(--ink)}

  .sport-card{position:absolute;left:53px;top:372px;width:314px;height:186px;border-radius:8px;background:var(--green-deep);padding:5px}
  .sport-card__media{position:relative;width:304px;height:176px;border-radius:6px;overflow:hidden;
    background:
      radial-gradient(ellipse 70px 55px at 46% 30%,rgba(255,248,225,.95),rgba(230,222,200,.55) 45%,rgba(0,0,0,0) 100%),
      linear-gradient(180deg,#c9c6bf 0%,#8d8b84 28%,#3b403b 52%,#1f2621 75%,#141a17 100%);}
  .sport-card__shade{position:absolute;inset:0;background:linear-gradient(180deg,rgba(0,0,0,0) 40%,rgba(0,0,0,.45) 100%)}
  .sport-card__text{position:absolute;left:19px;top:96px;width:180px;color:var(--white);font-size:10.5px;font-weight:700;line-height:19px}
  .action{position:absolute;width:18px;height:18px;border-radius:50%;background:var(--white);display:flex;align-items:center;justify-content:center}
  .touch-ring{position:absolute;left:254px;top:132px;width:60px;height:60px;border-radius:50%;background:rgba(255,255,255,.14)}
  .touch-dot{position:absolute;left:272px;top:146px;width:24px;height:24px;border-radius:50%;background:rgba(220,220,220,.9)}

  .composer{position:absolute;left:24px;top:648px;width:342px;height:41px;border-radius:8px;background:var(--white);box-shadow:0 0 0 1px rgba(0,0,0,.03)}
  .composer__placeholder{position:absolute;left:23px;top:12px;font-size:12px;line-height:16px;color:var(--muted)}
  .composer__send{position:absolute;left:304px;top:4px;width:33px;height:33px;border-radius:4px;background:var(--green-deep);display:flex;align-items:center;justify-content:center}
</style>
</head>
<body>
<div class="screen">
  <header class="app-bar">
    <svg class="app-bar__back" width="33" height="20" viewBox="0 0 33 20"><path d="M32 10H3M11 2 2 10l9 8" fill="none" stroke="#4a4a4a" stroke-width="2.6" stroke-linecap="round" stroke-linejoin="round"/></svg>
    <h1 class="app-bar__title">Chat</h1>
    <svg class="app-bar__menu" width="21" height="17" viewBox="0 0 21 17"><g stroke="#4a4a4a" stroke-width="2.6" stroke-linecap="round"><path d="M1.5 2h18M1.5 8.5h18M1.5 15h18"/></g></svg>
  </header>

  <div class="contact-bar">
    <div class="contact-bar__avatar" role="img" aria-label="Contact profile photo"></div>
    <span class="contact-bar__name">Dano K.</span>
    <span class="contact-bar__status">Online</span>
  </div>

  <main class="conversation">
    <div class="bubble-sent">Omnis iste natus error sit volupta</div>
    <span class="timestamp" style="top:330px">16:03</span>

    <article class="sport-card">
      <div class="sport-card__media" role="img" aria-label="Photo of a sports team huddled together at sunset">
        <div class="sport-card__shade"></div>
        <p class="sport-card__text">Lorem ipsum dolor sit amet, consec tetur adipiscing elit, sed do eiusmod tempor incidid.</p>

        <span class="action" style="left:251px;top:107px" aria-label="Website">
          <svg width="12" height="12" viewBox="0 0 12 12"><g fill="none" stroke="#111" stroke-width="1.1"><circle cx="6" cy="6" r="5"/><ellipse cx="6" cy="6" rx="2.2" ry="5"/><path d="M1 6h10M2 3.5h8M2 8.5h8"/></g></svg>
        </span>
        <span class="action" style="left:281px;top:101px" aria-label="Share">
          <svg width="12" height="12" viewBox="0 0 12 12"><g fill="#111"><circle cx="9" cy="2.5" r="2"/><circle cx="3" cy="6" r="2"/><circle cx="9" cy="9.5" r="2"/></g><path d="M9 2.5 3 6l6 3.5" stroke="#111" stroke-width="1.1" fill="none"/></svg>
        </span>
        <span class="action" style="left:232px;top:125px" aria-label="Email">
          <svg width="11" height="9" viewBox="0 0 11 9"><rect width="11" height="9" rx="1.5" fill="#111"/><path d="M1 1.5l4.5 3.5L10 1.5" stroke="#fff" stroke-width="1.1" fill="none"/></svg>
        </span>
        <span class="action" style="left:229px;top:152px" aria-label="Call">
          <svg width="11" height="11" viewBox="0 0 24 24"><path fill="#111" d="M6.6 10.8a15.1 15.1 0 0 0 6.6 6.6l2.2-2.2c.3-.3.7-.4 1-.2 1.1.4 2.3.6 3.6.6.6 0 1 .4 1 1V20c0 .6-.4 1-1 1A17 17 0 0 1 3 4c0-.6.4-1 1-1h3.5c.6 0 1 .4 1 1 0 1.3.2 2.5.6 3.6.1.3 0 .7-.2 1L6.6 10.8z"/></svg>
        </span>

        <div class="touch-ring"></div>
        <div class="touch-dot"></div>
      </div>
    </article>
    <span class="timestamp" style="top:570px">16:03</span>

    <div class="composer">
      <span class="composer__placeholder">Type here...</span>
      <span class="composer__send" aria-label="Send">
        <svg width="10" height="15" viewBox="0 0 10 15"><path d="M2 1.5 8 7.5 2 13.5" fill="none" stroke="#fff" stroke-width="1.8" stroke-linecap="round" stroke-linejoin="round"/></svg>
      </span>
    </div>
  </main>
</div>
</body>
</html>
```